Consulting company (stride-and-calm, previously stundenwerk lübeck) needs design for a clear and fre

This website is to be made completely new with Worpreess / Divi. I am at the beginning and have no idea about the design. The design is the focus of this order. After the first website I would like to use the design and colors for all other design products for business, which will be placed here as well.
On the website the services, the team, references ... should be separate pages. Please see the attached document. A very important part is the blog and the categories should be visible in the desktop view, vie widgets.

The site should be clear, well-arranged, but still convey freshness and vitality.
Our company offers consulting and online trainings for the following topics:
- Digital paperless office
- process optimization, digitalization
- Remote working and productivity
- Remote leadership
- remote project management
- Time management 4. 0
- Focus on the essentials

We do this in the form of:
- Keynote Speaking
- Facilitating
- Presentation
- Workshops and trainings
- Online trainings

Our services are intended exclusively for companies.

What drives us?
We want to inspire our customers to work more green, lean digital and focus on the essentials. We are a team of three people who are digital nomads, but who also work offline on site.
I do have already webseites, but they are old, but give you an idea what we do: stundenwerk-luebeck.example. and ms-inkfree.example.

One style of a web site I like is for example is that of "plenvoro.example" Colors I thought so far, but I'm not sure, could be the color palette "vandal pigment" from drafbel.example or something similar to # f60b80a and # 39dfa7. But I am open for other suggestions.
I love simple and clear fonts. I like this contemporary style of sites, where you get most of the content on the mobile devices by scrolling.

Target Market(s)

midsize and large businesses, decision maker

Logo Text

Stride and Calm Consulting

Number of Pages Required

5+ page

Font styles to use
Sans Serif

Colors
e34297
00a990

Requirements
Must have
• the page should be clear and concise, much white with color accents like content blocks or headlines, responsive,
Nice to have
• I like interesting backgrounds, very discreet, perhaps white and gray or the color shades of pastel, the site should somehow fit to the photos, the logo I added is the old one, just to give you an idea
Should not have
• in no case too playful or loud

```html
<!DOCTYPE html>
<html lang="en">
<head>
<meta charset="utf-8">
<title>Stride and Calm Consulting</title>
<link href="https://fonts.googleapis.com/css2?family=Mulish:wght@400;500;600&family=Quicksand:wght@500;600&family=Roboto:wght@400;500&display=swap" rel="stylesheet">
<style>
:root{
  --pink:#e5096f;
  --teal:#1a9a80;
  --ink:#333;
  --muted:#666;
  --soft:#f3f4f6;
  --line:#e4e4e4;
  --white:#fff;
}
*{box-sizing:border-box;margin:0;padding:0}
html,body{width:1200px;height:3139px;overflow:hidden;background:var(--white)}
body{font-family:'Mulish',sans-serif;color:var(--ink);position:relative}
a{color:inherit;text-decoration:none}

/* top bar */
.topbar{position:absolute;left:0;top:0;width:1200px;height:50px;background:var(--teal);color:var(--white);font-size:15px}
.topbar .social{position:absolute;left:110px;top:15px}
.topbar .contact{position:absolute;right:111px;top:15px;display:flex;gap:34px;align-items:center}
.topbar .contact span{display:flex;align-items:center;gap:7px}

/* header */
.header{position:absolute;left:0;top:50px;width:1200px;height:121px;background:var(--white);border-bottom:1px solid var(--line)}
.brand{position:absolute;left:111px;top:11px;display:flex;align-items:center;gap:16px}
.brand-dot{width:86px;height:86px;border-radius:50%;border:6px solid var(--teal)}
.brand-name{font-family:'Quicksand',sans-serif;font-weight:600;font-size:26px;line-height:30px;color:var(--teal)}
.nav{position:absolute;top:53px;left:0;font-size:15.5px;color:#222}
.nav a{position:absolute;white-space:nowrap}
.nav a.active{color:var(--pink)}

/* hero */
.hero{position:absolute;left:0;top:171px;width:1200px;height:770px;overflow:hidden}
.hero-photo{position:absolute;inset:0;background:linear-gradient(100deg,#dfe3e6 0%,#eef0f1 35%,#d9d6d4 60%,#c8c4c2 100%)}
.hero-curve{position:absolute;left:0;top:0}
.hero h1{position:absolute;left:111px;top:228px;font-family:'Quicksand',sans-serif;font-weight:600;font-size:50px;line-height:55px}
.hero h1 .l1{color:var(--pink);display:block}
.hero h1 .l2{color:var(--teal);display:block}
.btn{display:inline-flex;align-items:center;justify-content:center;background:var(--pink);color:var(--white);border-radius:30px}
.hero .btn{position:absolute;left:111px;top:360px;width:171px;height:47px;font-family:'Quicksand',sans-serif;font-size:20px;font-weight:500}
.dots{position:absolute;left:576px;top:882px;display:flex;gap:8px}
.dots i{width:10px;height:10px;border-radius:50%;background:var(--teal)}
.dots i.on{background:var(--pink)}

/* section title */
.sec-title{position:absolute;left:0;width:1200px;text-align:center;font-family:'Roboto',sans-serif;font-weight:400;font-size:29px;color:var(--pink)}
.sec-title::after{content:"";display:block;width:70px;height:3px;background:var(--pink);margin:12px auto 0}

/* services */
.services-sub{position:absolute;left:0;top:1047px;width:1200px;text-align:center;font-size:13px;color:var(--muted)}
.service{position:absolute;top:1109px;width:176px;height:176px}
.service svg{position:absolute;left:0;top:0}
.service .label{position:absolute;left:0;top:96px;width:176px;text-align:center;font-size:15px;line-height:19px}
.service.teal .label{color:var(--teal)}
.service.pink .label{color:var(--pink)}

/* about */
.about{position:absolute;left:0;top:1349px;width:1200px;height:512px;background:var(--soft)}
.about h2{position:absolute;left:111px;top:105px;font-family:'Roboto',sans-serif;font-weight:400;font-size:29px;color:var(--pink)}
.about h2::after{content:"";display:block;width:70px;height:3px;background:var(--pink);margin-top:12px}
.about p{position:absolute;left:111px;top:183px;width:320px;font-size:17px;line-height:28.3px;color:#555}
.about .btn{position:absolute;left:111px;top:377px;width:152px;height:47px;border-radius:24px;font-size:16px}
.photo-back{position:absolute;left:701px;top:58px;width:387px;height:389px;background:linear-gradient(135deg,#9fa7a6,#d7dadc 60%,#e8e9ea)}
.photo-front{position:absolute;left:520px;top:125px;width:280px;height:282px;background:linear-gradient(135deg,#d9d3cc,#f2f0ee 50%,#8a7f77);border:2px solid var(--white)}

/* testimonial */
.quote-band{position:absolute;left:0;top:1861px;width:1200px;height:286px;background:linear-gradient(100deg,#d9237a 0%,#b53a8a 35%,#7b4a96 60%,#2f8a8a 100%)}
.quote-card{position:absolute;left:203px;top:51px;width:794px;height:184px;background:rgba(255,255,255,.82);border-radius:3px}
.quote-mark{position:absolute;left:37px;top:27px;width:132px;height:132px;border-radius:50%;background:var(--pink);color:var(--white);display:flex;align-items:center;justify-content:center;font-size:18px;font-weight:600}
.quote-text{position:absolute;left:202px;top:63px;width:500px;font-size:15px;line-height:31px;color:#555}
.quote-text u{color:var(--teal)}
.quote-arrows{position:absolute;left:729px;top:80px;font-size:14px;color:#999;letter-spacing:10px}

/* blog */
.card{position:absolute;top:2272px;height:409px;background:var(--white);border:1px solid #eee;box-shadow:0 1px 4px rgba(0,0,0,.08)}
.card .img{height:232px;width:100%}
.card .meta{color:var(--teal);font-weight:500}
.card .meta span+span{margin-left:14px}
.card h3{font-weight:500;color:#333}
.card p{color:#555}
.card.wide{left:111px;width:495px}
.card.wide .meta{position:absolute;left:16px;top:254px;font-size:15px}
.card.wide h3{position:absolute;left:16px;top:292px;font-size:20px}
.card.wide p{position:absolute;left:18px;top:330px;width:450px;font-size:13px;line-height:26px}
.card.narrow{width:226px}
.card.narrow .meta{position:absolute;left:11px;top:251px;font-size:12px}
.card.narrow .meta span+span{margin-left:12px}
.card.narrow h3{position:absolute;left:11px;top:278px;width:210px;font-size:18.5px;line-height:30px}
.card.narrow p{position:absolute;left:11px;top:340px;width:210px;font-size:13px;line-height:26px}

/* footer */
.footer{position:absolute;left:0;top:2751px;width:1200px;height:388px;background:var(--teal);color:var(--white)}
.footer h4{position:absolute;top:58px;font-weight:400;font-size:20px;letter-spacing:.3px}
.f-brand{position:absolute;left:120px;top:145px;display:flex;align-items:center;gap:12px}
.f-brand .brand-dot{width:74px;height:74px;border:5px solid var(--white)}
.f-brand .brand-name{color:var(--white);font-size:21px;line-height:25px;font-weight:500}
.f-links{position:absolute;left:402px;top:107px;list-style:none;font-size:15px}
.f-links li{height:30px;display:flex;align-items:center}
.f-links li::before{content:"»";width:32px;font-size:14px}
.f-touch{position:absolute;left:608px;top:108px;font-size:13.5px;line-height:29.2px}
.f-news p{position:absolute;left:863px;top:108px;width:225px;font-size:12.5px;line-height:28px}
.f-input{position:absolute;left:863px;top:188px;width:225px;height:42px;background:var(--white);color:#444;font-size:12px;padding:14px 13px;border-radius:2px}
.f-submit{position:absolute;left:863px;top:240px;width:98px;height:35px;background:var(--pink);color:var(--white);font-size:14px;display:flex;align-items:center;justify-content:center}
.f-rule{position:absolute;left:111px;top:312px;width:977px;height:1px;background:rgba(255,255,255,.45)}
.f-copy{position:absolute;left:0;top:339px;width:1200px;text-align:center;font-size:14px}
</style>
</head>
<body>

<div class="topbar">
  <div class="social">Socialia | &nbsp;Worknet | &nbsp;Proflink</div>
  <div class="contact">
    <span><svg width="13" height="13" viewBox="0 0 24 24" fill="#fff"><path d="M6.6 10.8a15.1 15.1 0 0 0 6.6 6.6l2.2-2.2c.3-.3.7-.4 1-.2 1.1.4 2.3.6 3.6.6.6 0 1 .4 1 1V20c0 .6-.4 1-1 1A17 17 0 0 1 3 4c0-.6.4-1 1-1h3.5c.6 0 1 .4 1 1 0 1.3.2 2.5.6 3.6.1.3 0 .7-.2 1z"/></svg>Call us : 0000-555-0142</span>
    <span><svg width="14" height="12" viewBox="0 0 24 20" fill="none" stroke="#fff" stroke-width="2"><rect x="1" y="1" width="22" height="18" rx="2"/><path d="M1 3l11 8 11-8"/></svg>hello@strideandcalm.example</span>
  </div>
</div>

<header class="header">
  <div class="brand">
    <div class="brand-dot"></div>
    <div class="brand-name">Stride and Calm<br>Consulting</div>
  </div>
  <nav class="nav">
    <a class="active" style="left:520px">Home</a>
    <a style="left:602px">About Us</a>
    <a style="left:708px">Services</a>
    <a style="left:806px">Blog</a>
    <a style="left:878px">Testimonials</a>
    <a style="left:1008px">Contact Us</a>
  </nav>
</header>

<section class="hero">
  <div class="hero-photo" role="img" aria-label="Photo of a smiling consultant working on a laptop in a bright office"></div>
  <svg class="hero-curve" width="1200" height="770" viewBox="0 0 1200 770">
    <path d="M0,606 Q600,884 1200,606 L1200,606 Q600,916 0,606 Z" fill="#e5096f"/>
    <path d="M0,606 Q600,916 1200,606 L1200,770 L0,770 Z" fill="#fff"/>
  </svg>
  <h1><span class="l1">Work Focused</span><span class="l2">Stride and Calm</span></h1>
  <a class="btn">Learn More</a>
</section>
<div class="dots"><i></i><i class="on"></i><i></i></div>

<h2 class="sec-title" style="top:984px">OUR SERVICES</h2>
<p class="services-sub">Sed ut perspiciatis unde omnis iste natus error sit voluptatem accusantium doloremque laudantium</p>

<div class="service teal" style="left:111px">
  <svg width="176" height="176" viewBox="0 0 176 176" fill="none" stroke="#1a9a80" stroke-width="2.5">
    <circle cx="90" cy="88" r="85"/><path d="M1,74 L14,88 L1,102 Z" fill="#1a9a80"/>
    <rect x="68" y="28" width="44" height="20" rx="8"/><circle cx="74" cy="66" r="6"/><circle cx="104" cy="66" r="6"/>
    <path d="M63,84 q11,-14 22,0 M93,84 q11,-14 22,0"/>
  </svg>
  <div class="label">Keynote<br>Speaking</div>
</div>
<div class="service pink" style="left:311px">
  <svg width="176" height="176" viewBox="0 0 176 176" fill="none" stroke="#e5096f" stroke-width="2.5">
    <circle cx="90" cy="88" r="85"/><path d="M1,74 L14,88 L1,102 Z" fill="#e5096f"/>
    <rect x="64" y="44" width="52" height="36" rx="3"/><rect x="76" y="56" width="28" height="12"/><path d="M70,36 v8 M90,30 v14 M110,36 v8"/>
  </svg>
  <div class="label">Facilitating</div>
</div>
<div class="service teal" style="left:511px">
  <svg width="176" height="176" viewBox="0 0 176 176" fill="none" stroke="#1a9a80" stroke-width="2.5">
    <circle cx="90" cy="88" r="85"/><path d="M1,74 L14,88 L1,102 Z" fill="#1a9a80"/>
    <rect x="62" y="32" width="46" height="34"/><path d="M85,66 v14 M75,82 l10,-16 l10,16"/><circle cx="112" cy="42" r="5"/><path d="M112,48 v30"/>
  </svg>
  <div class="label">Presentation</div>
</div>
<div class="service pink" style="left:711px">
  <svg width="176" height="176" viewBox="0 0 176 176" fill="none" stroke="#e5096f" stroke-width="2.5">
    <circle cx="90" cy="88" r="85"/><path d="M1,74 L14,88 L1,102 Z" fill="#e5096f"/>
    <rect x="88" y="32" width="30" height="32"/><path d="M94,42 h18 M94,50 h18"/><circle cx="74" cy="46" r="8"/><path d="M60,78 q14,-22 28,0"/>
  </svg>
  <div class="label">Workshops<br>and Trainings</div>
</div>
<div class="service teal" style="left:911px">
  <svg width="176" height="176" viewBox="0 0 176 176" fill="none" stroke="#1a9a80" stroke-width="2.5">
    <circle cx="90" cy="88" r="85"/><path d="M1,74 L14,88 L1,102 Z" fill="#1a9a80"/>
    <path d="M64,34 h24 v40 h-24 z M92,34 h24 v40 h-24 z M60,80 h60"/><path d="M70,44 h12 M70,52 h12 M98,44 h12 M98,52 h12"/>
  </svg>
  <div class="label">Online<br>Trainings</div>
</div>

<section class="about">
  <h2>ABOUT US</h2>
  <p>Sed ut perspiciatis unde omnis iste nat us error sit voluptatem accusantium dol oremque laudantium, totam rem aperia riam, eaque ipsa quae ab illo inventore veritatis et quasi architecto beatae vitae dicta sunt explicabo</p>
  <a class="btn">LEARN MORE</a>
  <div class="photo-back" role="img" aria-label="Photo of a consultant working on a laptop at a meeting table"></div>
  <div class="photo-front" role="img" aria-label="Photo of two colleagues reviewing documents together"></div>
</section>

<section class="quote-band" role="img" aria-label="Background collage of portrait photos under a pink to teal tint">
  <div class="quote-card">
    <div class="quote-mark">Chirply</div>
    <p class="quote-text">Sed ut perspiciatis <u>unde omnis iste natus</u> error sit voluptatem accusa<br><u>ntium doloremque</u> laudantium, totam rem beatae</p>
    <div class="quote-arrows">‹ ›</div>
  </div>
</section>

<h2 class="sec-title" style="top:2196px">LATEST BLOG</h2>

<article class="card wide">
  <div class="img" role="img" aria-label="Photo of a training session with participants at laptops" style="background:linear-gradient(135deg,#6b5a4e,#b9a58f 45%,#e7e2da)"></div>
  <div class="meta"><span>by Lena Vogt</span><span>May 27, 2020</span></div>
  <h3>Sed ut perspiciatis unde omnis iste natus error</h3>
  <p>Sed ut perspiciatis unde omnis iste natus error sit voluptatem accusa ntium doloremque laudantium</p>
</article>
<article class="card narrow" style="left:623px">
  <div class="img" role="img" aria-label="Photo of two smiling business colleagues" style="background:linear-gradient(135deg,#c9d3de,#f1f3f5 50%,#5d6b7a)"></div>
  <div class="meta"><span>by Lena Vogt</span><span>May 27, 2020</span></div>
  <h3>Sed ut perspiciatis unde omnis iste natus</h3>
  <p>Sed ut perspiciatis unde omnis natus error sit voluptatem</p>
</article>
<article class="card narrow" style="left:863px">
  <div class="img" role="img" aria-label="Photo of a consultant writing on a whiteboard" style="background:linear-gradient(135deg,#e9ebee,#d8d4d0 55%,#8a7a70)"></div>
  <div class="meta"><span>by Lena Vogt</span><span>May 27, 2020</span></div>
  <h3>Sed ut perspiciatis unde omnis iste natus</h3>
  <p>Sed ut perspiciatis unde omnis natus error sit voluptatem</p>
</article>

<footer class="footer">
  <div class="f-brand">
    <div class="brand-dot"></div>
    <div class="brand-name">Stride and Calm<br>Consulting</div>
  </div>
  <h4 style="left:400px">LINKS</h4>
  <ul class="f-links">
    <li>Home</li><li>About Us</li><li>Services</li><li>Blog</li><li>Testimonials</li><li>Contact Us</li>
  </ul>
  <h4 style="left:606px">GET IN TOUCH</h4>
  <div class="f-touch">Tele : &nbsp;000-555-0142<br>Fax : &nbsp;000-555-0143<br>hello@strideandcalm.example<br>2710 Lorem Ipsum is simply<br>dummy text.</div>
  <h4 style="left:863px">NEWSLETTER</h4>
  <div class="f-news"><p>Sed ut perspiciatis unde error sit vol uptatem accusantium...</p></div>
  <div class="f-input">Enter Email Id :</div>
  <div class="f-submit">Submit</div>
  <div class="f-rule"></div>
  <div class="f-copy">© Copyright 2020 Stride and Calm.All Rights Reserved</div>
</footer>

</body>
</html>
```